Web design for a Crane & Heavy Equipment Inspection, Repair and Maintenance Company in Texas

We need a web design for a new company based in Houston, Texas called "Bristen Hoist & Equipment". We inspect, repair and maintain diesel driven heavy equipment, generators, fire water pumps and cranes. We would like to see designs that use the colors orange, white, yellow and brown, and/or orange, white, navy, yellow and grey.

```html
<!DOCTYPE html>
<html lang="en">
<head>
<meta charset="utf-8">
<title>Bristen Hoist &amp; Equipment</title>
<link href="https://fonts.googleapis.com/css2?family=Open+Sans:wght@400;600;700&display=swap" rel="stylesheet">
<style>
:root{
  --orange:#e05428;
  --orange-light:#f26a3c;
  --navy:#0d3b6e;
  --blue:#1e6bb8;
  --blue-dark:#0f4d93;
  --white:#ffffff;
  --grey:#9a9a9a;
  --grey-dark:#555a60;
  --photo-a:#9a6a4c;
  --photo-b:#3c3a3e;
}
*{margin:0;padding:0;box-sizing:border-box}
html,body{width:930px;height:1200px;overflow:hidden;background:var(--white)}
body{position:relative;font-family:'Open Sans',Arial,sans-serif;color:var(--grey-dark)}
.abs{position:absolute}
.brand{left:126px;top:36px;font-size:22px;font-weight:700;color:var(--orange);letter-spacing:.3px;line-height:1.1}
.brand-mark{display:inline-block;width:12px;height:12px;background:var(--orange);margin-right:7px;vertical-align:1px}
.search{left:682px;top:38px;width:122px;height:18px;display:flex}
.search-field{flex:1;border:1px solid #d6d6d6;border-right:none;border-radius:2px 0 0 2px;font-size:7px;color:#aaa;padding:4px 8px}
.search-btn{width:21px;background:var(--blue-dark);border-radius:0 2px 2px 0;display:flex;align-items:center;justify-content:center}
.nav{left:0;top:94px;width:930px;height:28px;background:linear-gradient(#2a7bc8,#135ca8);border-bottom:1px solid #0c4a8a}
.nav-item{position:absolute;top:0;height:28px;display:flex;align-items:center;justify-content:center;font-size:8px;color:var(--white);font-weight:600;border-left:1px solid #0f4f92}
.band{left:0;top:298px;width:930px;height:407px;background:var(--orange)}
.slider{left:125px;top:140px;width:680px;height:319px;background:linear-gradient(180deg,#a77556 0%,var(--photo-a) 40%,#5a4a4a 70%,var(--photo-b) 100%);box-shadow:0 18px 20px -10px rgba(0,0,0,.35)}
.slide-title{left:58px;top:75px;font-size:24px;color:var(--white);font-weight:400;letter-spacing:.2px}
.slide-copy{left:58px;top:125px;width:322px;font-size:9.6px;line-height:14px;color:var(--white);font-weight:600}
.slide-copy p+p{margin-top:14px}
.arrow{top:149px;width:20px;height:20px}
.dots{left:318px;top:299px;display:flex;gap:7px}
.dot{width:11px;height:11px;border:1.5px solid var(--white);border-radius:50%;display:flex;align-items:center;justify-content:center}
.dot.active::after{content:"";width:5px;height:5px;border-radius:50%;background:var(--white)}
.welcome-title{left:125px;top:501px;font-size:14.5px;color:var(--white);font-weight:600}
.welcome-copy{left:125px;top:543px;width:500px;font-size:9.7px;line-height:14px;color:var(--white)}
.welcome-copy p+p{margin-top:14px}
.btn-light{left:125px;top:646px;width:58px;height:19px;background:var(--white);color:var(--orange);font-size:8px;display:flex;align-items:center;justify-content:center}
.welcome-img{left:648px;top:530px;width:157px;height:111px;background:linear-gradient(180deg,#1d3550 0%,#3d5a78 45%,#c8905a 75%,#1a1a1a 100%);box-shadow:0 10px 12px -6px rgba(0,0,0,.4)}
.section-title{left:0;top:747px;width:930px;text-align:center;font-size:15px;color:var(--navy);font-weight:600}
.section-title span{color:var(--orange)}
.service{top:811px;width:220px;text-align:center}
.service-icon{width:87px;height:87px;margin:0 auto;border-radius:50%;background:var(--orange-light);border:2px solid var(--navy);display:flex;align-items:center;justify-content:center}
.service-name{margin-top:21px;font-size:12px;color:var(--grey-dark);font-weight:600}
.service-copy{margin-top:10px;font-size:9.6px;line-height:14px;color:var(--grey)}
.btn-dark{margin:13px auto 0;width:58px;height:18px;background:var(--blue-dark);color:var(--white);font-size:8px;display:flex;align-items:center;justify-content:center}
.footer{left:0;top:1081px;width:930px;height:93px;background:var(--navy)}
.footer-nav{left:0;top:30px;width:930px;display:flex;justify-content:center;align-items:center;font-size:8px;color:var(--white);font-weight:600}
.footer-nav .sep{width:3px;height:3px;border-radius:50%;background:#3f6c9c;margin:0 19px}
.social{left:0;top:58px;width:930px;display:flex;justify-content:center;gap:22px}
.social span{width:9px;height:9px;border-radius:50%;background:#3a6592}
.copyright{left:0;top:1180px;width:930px;text-align:center;font-size:8px;color:var(--grey)}
.copyright a{color:var(--navy);text-decoration:none}
</style>
</head>
<body>

<div class="abs brand"><span class="brand-mark"></span>BRISTEN HOIST &amp; EQUIPMENT</div>

<div class="abs search">
  <div class="search-field">Search...</div>
  <div class="search-btn"><svg width="9" height="9" viewBox="0 0 10 10"><circle cx="4" cy="4" r="3" fill="none" stroke="#fff" stroke-width="1.5"/><line x1="6.2" y1="6.2" x2="9" y2="9" stroke="#fff" stroke-width="1.6"/></svg></div>
</div>

<nav class="abs nav">
  <div class="nav-item" style="left:124px;width:91px">HOME</div>
  <div class="nav-item" style="left:215px;width:109px">ABOUT US</div>
  <div class="nav-item" style="left:324px;width:104px">SERVICES</div>
  <div class="nav-item" style="left:428px;width:127px">OUR PARTNERS</div>
  <div class="nav-item" style="left:555px;width:135px">WHY CHOOSE US</div>
  <div class="nav-item" style="left:690px;width:116px;border-right:1px solid #0f4f92">CONTACT US</div>
</nav>

<div class="abs band"></div>

<section class="abs slider" role="img" aria-label="Harbour cranes and a cargo ship at sunset">
  <h1 class="abs slide-title">BRISTEN HOIST &amp; EQUIPMENT</h1>
  <div class="abs slide-copy">
    <p>Lorem ipsum dolor sit amet, consectetur adipiscing elit. Mauris bibendum diam sapien, nec tristique tellus condimentum quis. Curabitur ut ipsum neque. Donec ultricies sollicitudin eros, at condimentum tellus vestibulum a. Morbi dapibus arcu eget justo pharetra dapibus.</p>
    <p>Curabitur ornare nisi sed nibh dapibus scelerisque. Etiam augue turpis, imperdiet fringilla vulputate id, cursus sit amet lorem. In viverra lacus metus. Integer bibendum vitae lorem vel fermentum.</p>
  </div>
  <svg class="abs arrow" style="left:15px" viewBox="0 0 20 20"><circle cx="10" cy="10" r="9" fill="none" stroke="#fff" stroke-width="1"/><polyline points="11.5,6.5 8,10 11.5,13.5" fill="none" stroke="#fff" stroke-width="1"/></svg>
  <svg class="abs arrow" style="left:645px" viewBox="0 0 20 20"><circle cx="10" cy="10" r="9" fill="none" stroke="#fff" stroke-width="1"/><polyline points="8.5,6.5 12,10 8.5,13.5" fill="none" stroke="#fff" stroke-width="1"/></svg>
  <div class="abs dots"><span class="dot active"></span><span class="dot"></span><span class="dot"></span></div>
</section>

<h2 class="abs welcome-title">WELCOME TO BRISTEN HOIST</h2>
<div class="abs welcome-copy">
  <p>Lorem ipsum dolor sit amet, consectetur adipiscing elit. Mauris bibendum diam sapien, nec tristique tellus condimentum quis. Curabitur ut ipsum neque. Donec ultricies sollicitudin eros, at condimentum tellus vestibulum a. Morbi dapibus arcu eget justo pharetra dapibus. Curabitur ornare nisi sed nibh dapibus scelerisque. Etiam augue turpis, imperdiet fringilla vulputate id, cursus sit amet lorem.</p>
  <p>&nbsp;In viverra lacus metus. Integer bibendum vitae lorem vel fermentum. Donec eget feugiat leo. Phasellus commodo</p>
</div>
<div class="abs btn-light">READ MORE</div>
<div class="abs welcome-img" role="img" aria-label="Silhouetted dock cranes against a dusk sky"></div>

<h2 class="abs section-title">WHAT <span>WE DO</span></h2>

<div class="abs service" style="left:122px">
  <div class="service-icon"><svg width="26" height="18" viewBox="0 0 26 18"><path d="M1 9 Q13 -4 25 9 Q13 22 1 9Z" fill="#fff"/><circle cx="13" cy="9" r="4.5" fill="var(--orange-light)"/><circle cx="13" cy="9" r="2.3" fill="#fff"/></svg></div>
  <div class="service-name">Inspection</div>
  <div class="service-copy">Lorem ipsum dolor sit amet, consectetur adipiscing elit. Mauris bibendum diam sapien, nec tristique tellus condimentum quis</div>
  <div class="btn-dark">READ MORE</div>
</div>
<div class="abs service" style="left:355px">
  <div class="service-icon"><svg width="26" height="24" viewBox="0 0 26 24"><g fill="#fff"><circle cx="9" cy="13" r="6"/><g stroke="#fff" stroke-width="3"><line x1="9" y1="4" x2="9" y2="22"/><line x1="0" y1="13" x2="18" y2="13"/><line x1="3" y1="7" x2="15" y2="19"/><line x1="15" y1="7" x2="3" y2="19"/></g><circle cx="20" cy="6" r="3.5"/><g stroke="#fff" stroke-width="2"><line x1="20" y1="1" x2="20" y2="11"/><line x1="15" y1="6" x2="25" y2="6"/></g><circle cx="20" cy="18" r="3.5"/><g stroke="#fff" stroke-width="2"><line x1="20" y1="13" x2="20" y2="23"/><line x1="15" y1="18" x2="25" y2="18"/></g></g><circle cx="9" cy="13" r="2.3" fill="var(--orange-light)"/><circle cx="20" cy="6" r="1.3" fill="var(--orange-light)"/><circle cx="20" cy="18" r="1.3" fill="var(--orange-light)"/></svg></div>
  <div class="service-name">Maintenance</div>
  <div class="service-copy">Lorem ipsum dolor sit amet, consectetur adipiscing elit. Mauris bibendum diam sapien, nec tristique tellus condimentum quis</div>
  <div class="btn-dark">READ MORE</div>
</div>
<div class="abs service" style="left:588px">
  <div class="service-icon"><svg width="26" height="26" viewBox="0 0 26 26"><line x1="4" y1="22" x2="15" y2="11" stroke="#fff" stroke-width="4.5" stroke-linecap="round"/><circle cx="18" cy="8" r="6.5" fill="#fff"/><path d="M18 8 L26 0 L26 4 L22 8Z" fill="var(--orange-light)"/><rect x="17" y="1" width="5" height="7" transform="rotate(45 19.5 4.5)" fill="var(--orange-light)"/><circle cx="5" cy="21" r="1" fill="var(--orange-light)"/></svg></div>
  <div class="service-name">Repairment</div>
  <div class="service-copy">Lorem ipsum dolor sit amet, consectetur adipiscing elit. Mauris bibendum diam sapien, nec tristique tellus condimentum quis</div>
  <div class="btn-dark">READ MORE</div>
</div>

<footer class="abs footer">
  <div class="abs footer-nav">
    <span>HOME</span><span class="sep"></span><span>ABOUT US</span><span class="sep"></span><span>SERVICES</span><span class="sep"></span><span>OUR PARTNERS</span><span class="sep"></span><span>WHY CHOOSE US</span><span class="sep"></span><span>CONTACT US</span>
  </div>
  <div class="abs social"><span></span><span></span><span></span></div>
</footer>
<div class="abs copyright">Copyright © 2014 BRISTEN HOIST - All Rights Reserved. <a>Terms and Conditions</a> <a>- Privacy Policy</a></div>

</body>
</html>
```